Personal Business Card Design Project

I am looking for a business card to be able to hand to both Chinese and Australian businessman.
I am a self employed consultant and just need my name, phone number and email address on the card. No Business Name and No Website.
I want it to look like an exclusive prestigious card.
I would like the background to be be a glossy red and the writing to be gold. (This applies to both sides of the card).
It must have English on one side and Chinese (Mandarin) on the reverse.
Details you will require
Name : Derek Hollins
Phone : + 61 428 903 574
Email : derekhollins@mailvanto.com
Updates
Thank you everybody for your designs.
Industry/Entity Type
Business

```html
<!DOCTYPE html>
<html lang="en">
<head>
<meta charset="utf-8">
<title>Derek Hollins — Business Card</title>
<link rel="stylesheet" href="https://fonts.googleapis.com/css2?family=Noto+Sans+SC:wght@600;700&family=Open+Sans:wght@600;700&display=swap">
<style>
  :root {
    --page-bg: #e9e4dc;
    --card-red-light: #a5161d;
    --card-red-mid: #990a0e;
    --card-red-dark: #7e0000;
    --gold: #cdb062;
    --icon-ink: #140404;
  }
  html, body {
    margin: 0;
    width: 1200px;
    height: 1200px;
    overflow: hidden;
    background: var(--page-bg);
  }
  .canvas {
    position: relative;
    width: 1200px;
    height: 1200px;
  }
  .business-card {
    position: absolute;
    left: 170px;
    width: 860px;
    height: 492px;
    background:
      radial-gradient(ellipse 90% 110% at 78% 8%, var(--card-red-light) 0%, var(--card-red-mid) 45%, var(--card-red-dark) 100%);
    box-shadow: 0 16px 36px rgba(0,0,0,0.28);
    font-family: "Open Sans", "Myriad Pro", Arial, sans-serif;
    color: var(--gold);
  }
  .card-front { top: 76px; }
  .card-back  { top: 632px; }
  .card-back .card-name {
    font-family: "Noto Sans SC", "Open Sans", sans-serif;
    letter-spacing: 2px;
  }
  .card-name {
    position: absolute;
    left: 114px;
    top: 222px;
    margin: 0;
    font-size: 45px;
    font-weight: 700;
    line-height: 60px;
    white-space: nowrap;
  }
  .contact-line {
    position: absolute;
    left: 90px;
    margin: 0;
    font-weight: 600;
    font-size: 34px;
    line-height: 46px;
    display: flex;
    align-items: center;
    white-space: nowrap;
  }
  .contact-phone { top: 310px; }
  .contact-email { top: 384px; }
  .contact-icon-slot {
    flex: none;
    width: 58px;
    margin-right: 16px;
    display: flex;
    justify-content: center;
  }
</style>
</head>
<body>
<main class="canvas">
  <section class="business-card card-front" aria-label="Business card, English side">
    <h1 class="card-name">Derek Hollins</h1>
    <p class="contact-line contact-phone">
      <span class="contact-icon-slot">
        <svg width="40" height="45" viewBox="0 0 46 52" aria-hidden="true">
          <path fill="var(--icon-ink)" d="M9 2c3-2 6-1 7 2l4 9c1 3 0 5-2 6l-3 2c1 6 5 12 10 16l3-2c2-1 4-1 6 1l6 7c2 2 2 5-1 7l-4 3c-4 2-9 1-14-3C11 42 4 30 3 18 2 11 4 6 9 2z"/>
        </svg>
      </span>
      + 61 428 903 574
    </p>
    <p class="contact-line contact-email">
      <span class="contact-icon-slot">
        <svg width="56" height="39" viewBox="0 0 66 46" aria-hidden="true">
          <g fill="none" stroke="var(--icon-ink)" stroke-width="3" stroke-linejoin="round">
            <rect x="2" y="2" width="62" height="42"/>
            <path d="M2 2l31 24L64 2"/>
            <path d="M2 44l23-22M64 44L41 22"/>
          </g>
        </svg>
      </span>
      derekhollins@mailvanto.com
    </p>
  </section>

  <section class="business-card card-back" lang="zh-Hans" aria-label="Business card, Chinese side">
    <h2 class="card-name">德里克·霍林斯</h2>
    <p class="contact-line contact-phone">
      <span class="contact-icon-slot">
        <svg width="40" height="45" viewBox="0 0 46 52" aria-hidden="true">
          <path fill="var(--icon-ink)" d="M9 2c3-2 6-1 7 2l4 9c1 3 0 5-2 6l-3 2c1 6 5 12 10 16l3-2c2-1 4-1 6 1l6 7c2 2 2 5-1 7l-4 3c-4 2-9 1-14-3C11 42 4 30 3 18 2 11 4 6 9 2z"/>
        </svg>
      </span>
      + 61 428 903 574
    </p>
    <p class="contact-line contact-email">
      <span class="contact-icon-slot">
        <svg width="56" height="39" viewBox="0 0 66 46" aria-hidden="true">
          <g fill="none" stroke="var(--icon-ink)" stroke-width="3" stroke-linejoin="round">
            <rect x="2" y="2" width="62" height="42"/>
            <path d="M2 2l31 24L64 2"/>
            <path d="M2 44l23-22M64 44L41 22"/>
          </g>
        </svg>
      </span>
      derekhollins@mailvanto.com
    </p>
  </section>
</main>
</body>
</html>
```